KTO Reception Posterboards

We need 3 posterboard designs for an upcoming reception. I will take your designs and have a local printer put them on foam poster board. I'll need the following please 1) Autos Move By Rail and 2) Safety

On the auto board, please include a big, prominent "3/4 of all autos move by rail." Some type of big, bold splash.

Please make sure the KTO logo is on the bottom right corner of each design.

As a side note, our poster boards are about 2 x 3 ft in size.

Target Market(s)

public officials

Industry/Entity Type

Printer

Requirements
Must have
• bold feel for the poster boards
Nice to have
• Include pics.

```html
<!DOCTYPE html>
<html lang="en">
<head>
<meta charset="UTF-8">
<title>Moving the American Auto Industry on Steel Wheels</title>
<link rel="stylesheet" href="https://fonts.googleapis.com/css2?family=Open+Sans:wght@400;700;800&family=Tinos:wght@400&display=swap">
<style>
  :root {
    --navy: #0e1a6e;
    --white: #ffffff;
    --paper: #f1f2f4;
    --ink: #2f2f2f;
    --sky-top: #f3f4f6;
    --sky-mid: #c5ced8;
    --train-gold: #c9a23c;
    --train-olive: #6f6a36;
    --inset-steel: #b8bcc2;
    --inset-rust: #7a2e22;
  }
  * { box-sizing: border-box; margin: 0; padding: 0; }
  html, body {
    width: 930px; height: 1200px; overflow: hidden; background: var(--paper);
  }
  .poster {
    position: relative; width: 930px; height: 1200px; overflow: hidden; background: var(--paper);
  }
  .header {
    position: absolute; left: 0; top: 0; width: 930px; height: 235px;
    background: var(--navy); color: var(--white);
    font-family: "Tinos", "Times New Roman", serif; text-align: center;
    padding-top: 34px; line-height: 1.05;
  }
  .header .lead { font-size: 80px; letter-spacing: 1px; }
  .header .sub { font-size: 48px; letter-spacing: 0.5px; margin-top: 4px; }
  .hero-photo {
    position: absolute; left: 0; top: 235px; width: 930px; height: 900px;
    background: linear-gradient(180deg, var(--sky-top) 0%, var(--sky-top) 22%, var(--sky-mid) 42%, var(--train-gold) 58%, #a98e3e 75%, var(--train-olive) 92%);
  }
  .intro {
    position: absolute; left: 110px; top: 262px; width: 710px;
    font-family: "Open Sans", Arial, sans-serif; font-weight: 700;
    font-size: 30px; line-height: 1.42; color: var(--ink);
  }
  .intro .line { display: block; text-align: justify; text-align-last: justify; }
  .intro .line.last { text-align: center; text-align-last: center; }
  .inset-photo {
    position: absolute; left: 568px; top: 480px; width: 240px; height: 310px;
    border-radius: 10px;
    background: linear-gradient(160deg, var(--inset-steel) 0%, #e4ddc8 40%, var(--inset-rust) 70%, #3a3a3a 100%);
  }
  .stat-splash {
    position: absolute; left: 70px; top: 560px; width: 320px; height: 320px;
    border-radius: 50%; background: var(--navy); border: 8px solid var(--white);
    display: flex; flex-direction: column; align-items: center; justify-content: center;
    text-align: center; color: var(--white);
    font-family: "Open Sans", Arial, sans-serif;
  }
  .stat-splash .figure { font-size: 108px; font-weight: 800; line-height: 1; }
  .stat-splash .label { font-size: 27px; font-weight: 700; line-height: 1.2; margin-top: 8px; text-transform: uppercase; }
  .footer-band { position: absolute; left: 0; top: 0; width: 930px; height: 1200px; }
  .brand {
    position: absolute; right: 42px; top: 948px; width: 150px; text-align: center;
    font-family: "Tinos", "Times New Roman", serif; color: var(--navy);
  }
  .brand .initials { font-size: 50px; line-height: 1; letter-spacing: 1px; }
  .brand .name { font-size: 15px; line-height: 1.15; letter-spacing: 1px; text-transform: uppercase; margin-top: 6px; }
  .site-url {
    position: absolute; left: 0; top: 1098px; width: 930px; text-align: center;
    font-family: "Open Sans", Arial, sans-serif; font-size: 22px; color: var(--navy);
  }
</style>
</head>
<body>
  <main class="poster">
    <div class="hero-photo" role="img" aria-label="Yellow enclosed autorack freight cars on a rail line beneath a cloudy sky"></div>

    <header class="header">
      <div class="lead">MOVING THE</div>
      <div class="sub">AMERICAN AUTO INDUSTRY</div>
      <div class="sub">ON STEEL WHEELS</div>
    </header>

    <p class="intro">
      <span class="line">Freight railroads are a reliable and nimble</span>
      <span class="line">partner of U.S. automakers, laying the</span>
      <span class="line">ground work for continued growth</span>
      <span class="line last">and vehicle sales that span the globe.</span>
    </p>

    <div class="inset-photo" role="img" aria-label="Open autorack car end showing pickup trucks loaded on two decks"></div>

    <div class="stat-splash">
      <div class="figure">3/4</div>
      <div class="label">of all autos<br>move by rail</div>
    </div>

    <svg class="footer-band" viewBox="0 0 930 1200" aria-hidden="true">
      <path d="M0 1045 C 300 1010, 620 960, 930 925 L930 1200 L0 1200 Z" fill="var(--white)"/>
      <rect x="0" y="1150" width="930" height="50" fill="var(--navy)"/>
    </svg>

    <div class="brand">
      <div class="initials">KTO</div>
      <div class="name">Keystone Transit Organization</div>
    </div>

    <div class="site-url">www.KeystoneTransitOrg.com</div>
  </main>
</body>
</html>
```